Hospital Website Design - PSD only

We need a web design for a community hospital based in Uniontown, Pennsylvania.

We would like to see a first round of designs for the website HOMEPAGE. Once we have selected finalists for the look & feel, based on the submitted homepage designs, we will request an additional INTERNAL page design.

Both designs should follow the content requirements displayed on the attached wireframes. I will post the internal page wireframe after the homepage design finalists are selected.

The desired Look & Feel for the website is clean and modern.

3 sites we like are:
http://www.marvellcare.org/
http://www.qrtm.org/
http://www.dellwyn.org/

Attached are the Homepage wireframe, and the Brackfield Hospital Logo.

The winning design will communicate a bright, healthy, energetic, community-oriented feeling.

Please note that readability is very important for a hospital website. Font-sizes and line-heights should be carefully selected for comfortable reading.
Updates

Dear designers -- Please don't feel locked into the exact shades of blue / brown used in the logo. We find this color scheme quite ugly and are working on a logo update. The new color scheme will probably still involve some shades of blue and brown, but we aren't sure yet. Please use your best judgement to make a beautiful design, similar in style to the modern / simple aesthetic of http://www.marvellcare.org/ We will be working on feedback to designs today. Thank you.

Regarding Large Rotating Graphic area and Navigation: We prefer a full-width display, rather than boxed. The navigation should be visually prominent, easy to read text that one can scan easily across the top of the page. Again, please refer to http://www.marvellcare.org/ for our preferred design aesthetic. Some of the designs submitted have been somewhat dated in their styling. We'd like a polished, modern, crisp, bold, beautiful design.

Re: choice of image in large rotating graphic area -- Designers, please do not use stock photography of a group of doctors, or a nursing home scene, in your sample rotating graphic areas. Although this should not affect our perception of the design, it throws off everything in the page if we don't like the image. Please try to select a bold / attractive image that you would like to set the tone for your design.

Reason: Extending our deadline to receive more designs exploring other color options containing less brown, or browns with a more attractive vibe. We would also like to see designs that are not exact replicas of the wireframe. The wireframe is just to show the elements on the page. Please use your creativity to utilize these elements in an attractive layout that we will like. We would also prefer to see use of photography that shows a younger, more cheerful, hopeful feeling in the design... and where the photographs are consistent with your design approach. Thanks!

In general, feedback for everyone is, please look here: http://www.marvellcare.org/ that's the feeling / vibe we want. DO NOT let the old, ugly, outdated logo determine your design. We are having the logo redesigned. DO NOT take an ugly, outdated template, and adapt it for this website. We want to see something BEAUTIFUL!!! Please give us your best effort! People who come to this website are in health crisis, and they want to be uplifted!! Their good spirits are in your hands.

Reason: We are still reviewing submissions and working with designers to provide better feedback. Thanks for your patience.

Reason: our sincerest apologies for the failure to provide adequate feedback this week. We hit a snag with the various decision makers on this project and were not able to review the recent submissions. We will make every effort to have a decision by tomorrow. Thank you for your patience.

Target Market(s)

Adults based in suburban & rural community, aged 18-80.

Industry/Entity Type

Hospital

Requirements
Must have
• The design must include all of the content areas outlined on the attached wireframe.
The design must include the attached logo. (Note, we may update the logo during the design contest, but it will not be changed dramatically. It will just be modernized slightly.)
Nice to have
• Show hover states for things like Navigation, Links, or small images in gallery, so we can see how you imagine interactive states.

```html
<!DOCTYPE html>
<html lang="en">
<head>
<meta charset="utf-8">
<title>Brackfield Hospital</title>
<link href="https://fonts.googleapis.com/css2?family=Josefin+Sans:wght@400;600;700&family=Open+Sans:wght@400;600&display=swap" rel="stylesheet">
<style>
:root{
  --teal:#3aaebf;
  --teal-dark:#2b8f9e;
  --coral:#f4594b;
  --ink:#1f1f1f;
  --grey-bg:#efefef;
  --panel:#f5f5f5;
  --footer:#2b2b2b;
  --footer-deep:#222;
  --muted:#8a8a8a;
  --white:#fff;
}
*{margin:0;padding:0;box-sizing:border-box}
html,body{width:738px;height:1200px;overflow:hidden}
body{position:relative;background:var(--white);font-family:"Josefin Sans",sans-serif;color:var(--ink)}
.abs{position:absolute}
a{color:inherit;text-decoration:none}

/* header */
.site-header{left:0;top:0;width:738px;height:70px;background:#f2f2f2}
.brand{left:20px;top:13px;display:flex;align-items:center;gap:10px}
.brand-mark{width:44px;height:44px;border-radius:50%;background:var(--teal)}
.brand-name{color:#222;font-weight:600;line-height:1;text-align:center}
.brand-name .l1{display:block;font-size:27px;letter-spacing:.5px}
.brand-name .l2{display:block;font-size:15px;letter-spacing:2px;margin-top:3px}
.util-nav{left:405px;top:30px;font-size:9px;font-weight:400;letter-spacing:.2px;display:flex;gap:6px;white-space:nowrap}
.top-search{left:566px;top:21px;width:168px;height:27px;background:var(--white);border-radius:4px}
.top-search svg{position:absolute}

/* nav */
.main-nav{left:0;top:70px;width:738px;height:44px;background:var(--teal)}
.main-nav a{position:absolute;top:18px;color:var(--white);font-size:9px;font-weight:600;letter-spacing:0;white-space:nowrap}

/* hero */
.hero{left:0;top:114px;width:738px;height:274px;background:radial-gradient(ellipse at 40% 40%,#5d86c2 0%,#2f5a99 35%,#13233f 80%,#0b1424 100%)}
.hero-title{left:0;top:222px;width:738px;text-align:center;color:var(--white)}
.hero-title h1{font-size:33px;font-weight:600;letter-spacing:1px}
.hero-title p{font-size:15.5px;font-weight:600;margin-top:4px;letter-spacing:.2px}

/* condition search + quick links */
.condition-box{left:10px;top:408px;width:310px;height:82px;background:var(--teal)}
.condition-box label{position:absolute;left:20px;top:19px;color:var(--white);font-size:11px}
.condition-input{position:absolute;left:16px;top:38px;width:267px;height:28px;background:var(--white);border-radius:4px;font-size:10.5px;padding:9px 0 0 28px;color:#333}
.condition-input svg{position:absolute}
.quick-link{width:90px;text-align:center;font-family:"Open Sans",sans-serif;font-size:10.5px;line-height:1.1;color:#222}
.quick-link svg{display:block;margin:0 auto 4px}

/* middle */
.mid-band{left:0;top:523px;width:360px;height:169px;background:#dcdcdc}
.photo-grid{left:6px;top:531px;width:181px;height:152px;display:grid;grid-template-columns:repeat(3,1fr);gap:5px}
.photo-grid div{background:linear-gradient(135deg,#8aa8c4,#5f7f99 55%,#c9d4dc)}
.photo-grid div:nth-child(3n+2){background:linear-gradient(180deg,#2f8f8a,#76b6a8 60%,#1d5b5a)}
.video{left:195px;top:531px;width:160px;height:152px;background:#000}
.panel-head{height:26px;background:var(--teal);color:var(--white);font-size:12px;padding:8px 0 0 13px}
.visit{left:367px;top:523px;width:178px;height:168px;background:var(--panel)}
.visit ul{list-style:none;padding:5px 0 0 15px}
.visit li{font-family:"Open Sans",sans-serif;font-size:8.6px;line-height:14.9px;color:#333;display:flex;align-items:center}
.visit li::before{content:"";display:inline-block;width:22px;height:1px;background:#3a5f9a;margin-right:13px}
.portal{left:552px;top:522px;width:186px;height:65px;background:var(--coral);color:var(--white)}
.portal .t{position:absolute;left:52px;top:7px;font-size:11px;line-height:12px}
.portal .btn{position:absolute;left:55px;top:36px;width:118px;height:22px;border:1px solid var(--white);font-size:10.5px;text-align:center;padding-top:5px;background:#e24536}
.resources{left:552px;top:590px;width:186px;height:101px;background:var(--panel)}
.resources li{list-style:none;font-family:"Open Sans",sans-serif;font-size:8.4px;color:#333;display:flex;align-items:center;gap:8px;margin:7px 0 0 8px;white-space:nowrap}
.resources li span.i{width:13px;height:13px;border:1px solid var(--coral);border-radius:50%;color:var(--coral);font-size:11px;line-height:11px;text-align:center;flex:none}

/* news */
.news-tabs{left:0;top:708px;width:738px;height:44px;background:#f6f6f6}
.tab-active{left:0;top:708px;width:130px;height:44px;background:var(--coral);color:var(--white);font-size:13px;padding:18px 0 0 17px}
.tab{left:138px;top:725px;font-size:13px;color:#222}
.news-band{left:0;top:752px;width:738px;height:221px;background:var(--coral)}
.story{width:130px;color:var(--white);font-family:"Open Sans",sans-serif;font-size:8.2px;line-height:10.5px;font-weight:600}
.hex{position:absolute}
.see-all{left:287px;top:932px;width:131px;height:29px;background:#111;color:var(--white);font-size:12px;text-align:center;padding-top:9px}

/* footer */
.footer{left:0;top:973px;width:738px;height:160px;background:var(--footer)}
.field{border-bottom:1px solid #555;color:#777;font-family:"Open Sans",sans-serif;font-size:9.5px;padding-bottom:4px}
.msg{left:246px;top:1014px;width:144px;height:44px;border:1px solid #555}
.send{left:67px;top:1078px;width:323px;height:28px;background:#1b1b1b;color:var(--white);font-size:8.5px;text-align:center;padding-top:10px;letter-spacing:.5px}
.contact{left:522px;color:#9a9a9a;font-family:"Open Sans",sans-serif;font-size:8px;letter-spacing:.4px;line-height:10px;padding-left:14px;border-left:1px solid #444}
.contact b{font-weight:600;display:block}
.contact .big{font-size:9.5px;color:#aaa}
.footer-bottom{left:0;top:1133px;width:738px;height:67px;background:var(--footer-deep);border-top:1px solid #555}
.bottom-links{left:5px;top:1167px;color:var(--white);font-family:"Open Sans",sans-serif;font-size:8.5px;white-space:nowrap}
.social{top:1151px;width:19px;height:19px;border:1px solid #444;border-radius:50%}
.copy{right:8px;top:1178px;color:#bbb;font-family:"Open Sans",sans-serif;font-size:8.5px}
</style>
</head>
<body>

<header class="site-header abs">
  <div class="brand abs">
    <span class="brand-mark"></span>
    <span class="brand-name"><span class="l1">BRACKFIELD</span><span class="l2">HOSPITAL</span></span>
  </div>
  <nav class="util-nav abs"><a href="#">ABOUT US</a><span>|</span><a href="#">NEWS</a><span>|</span><a href="#">GIVING</a></nav>
  <div class="top-search abs">
    <svg style="left:6px;top:6px" width="15" height="15" viewBox="0 0 15 15"><circle cx="6" cy="6" r="4.5" fill="none" stroke="#222" stroke-width="2"/><line x1="9.5" y1="9.5" x2="14" y2="14" stroke="#222" stroke-width="2.2"/></svg>
    <svg style="right:8px;top:7px" width="13" height="13" viewBox="0 0 13 13"><circle cx="6.5" cy="6.5" r="6.5" fill="#111"/><path d="M4 4l5 5M9 4l-5 5" stroke="#fff" stroke-width="1.6"/></svg>
  </div>
</header>

<nav class="main-nav abs">
  <a href="#" style="left:13px">HOME</a>
  <a href="#" style="left:70px">OUR SERVICES</a>
  <a href="#" style="left:156px">FACILITIES &amp; DIRECTIONS</a>
  <a href="#" style="left:306px">PATIENT &amp; VISITOR INFORMATION</a>
  <a href="#" style="left:483px">FIND A DOCTOR</a>
  <a href="#" style="left:582px">HEALTH &amp; WELLNESS</a>
</nav>

<section class="hero abs" role="img" aria-label="Blurred blue photograph of a cancer care treatment room"></section>
<div class="hero-title abs">
  <h1>CANCER CARE CENTER</h1>
  <p>THE BEST DOCTORS AND NURSES AND TREATMENT CLOSE TO HOME</p>
</div>

<div class="condition-box abs">
  <label>Do your want to learn about a condition?</label>
  <div class="condition-input">
    <svg style="left:8px;top:7px" width="14" height="14" viewBox="0 0 15 15"><circle cx="6" cy="6" r="4.5" fill="none" stroke="#222" stroke-width="2"/><line x1="9.5" y1="9.5" x2="14" y2="14" stroke="#222" stroke-width="2.2"/></svg>
    Diabetes, Cancer, Heart, Health, ....
    <svg style="right:6px;top:5px" width="17" height="17" viewBox="0 0 13 13"><circle cx="6.5" cy="6.5" r="6.5" fill="#111"/><path d="M4 4l5 5M9 4l-5 5" stroke="#fff" stroke-width="1.4"/></svg>
  </div>
</div>

<a class="quick-link abs" href="#" style="left:331px;top:402px"><svg width="58" height="58" viewBox="0 0 58 58"><circle cx="29" cy="29" r="27" fill="none" stroke="var(--teal)" stroke-width="1.5" stroke-dasharray="3 2"/><circle cx="29" cy="29" r="22" fill="var(--teal)"/><circle cx="29" cy="29" r="12" fill="none" stroke="#fff" stroke-width="2"/><path d="M29 22v14M22 29h14" stroke="#fff" stroke-width="3"/></svg>Symptom<br>Checker</a>
<a class="quick-link abs" href="#" style="left:442px;top:402px"><svg width="58" height="58" viewBox="0 0 58 58"><circle cx="29" cy="29" r="27" fill="none" stroke="var(--teal)" stroke-width="1.5" stroke-dasharray="3 2"/><circle cx="29" cy="29" r="22" fill="var(--teal)"/><circle cx="29" cy="29" r="12" fill="none" stroke="#fff" stroke-width="2"/><path d="M29 22v14M22 29h14" stroke="#fff" stroke-width="3"/></svg>Schedule a<br>Lab Test</a>
<a class="quick-link abs" href="#" style="left:542px;top:402px"><svg width="58" height="58" viewBox="0 0 58 58"><circle cx="29" cy="29" r="27" fill="none" stroke="var(--teal)" stroke-width="1.5" stroke-dasharray="3 2"/><circle cx="29" cy="29" r="22" fill="var(--teal)"/><circle cx="29" cy="29" r="12" fill="none" stroke="#fff" stroke-width="2"/><path d="M29 22v14M22 29h14" stroke="#fff" stroke-width="3"/></svg>Online<br>Bill Pay</a>
<a class="quick-link abs" href="#" style="left:639px;top:402px"><svg width="58" height="58" viewBox="0 0 58 58"><circle cx="29" cy="29" r="27" fill="none" stroke="var(--teal)" stroke-width="1.5" stroke-dasharray="3 2"/><circle cx="29" cy="29" r="22" fill="var(--teal)"/><circle cx="29" cy="29" r="12" fill="none" stroke="#fff" stroke-width="2"/><path d="M29 22v14M22 29h14" stroke="#fff" stroke-width="3"/></svg>Support<br>Our Work</a>

<div class="mid-band abs"></div>
<div class="photo-grid abs" role="img" aria-label="Gallery of hospital photographs: surgical team and corridor">
  <div></div><div></div><div></div><div></div><div></div><div></div><div></div><div></div><div></div>
</div>
<div class="video abs">
  <svg class="abs" style="left:47px;top:35px" width="62" height="68" viewBox="0 0 62 68"><polygon points="31,3 58,18 58,50 31,65 4,50 4,18" fill="#fff" stroke="#fff"/><polygon points="31,8 54,21 54,47 31,60 8,47 8,21" fill="#111"/><polygon points="25,23 42,34 25,45" fill="#fff"/></svg>
  <div class="abs" style="left:4px;top:140px;width:150px;height:2px;background:#555"></div>
  <div class="abs" style="left:4px;top:140px;width:60px;height:2px;background:#ccc"></div>
  <div class="abs" style="left:4px;top:145px;width:150px;height:3px;border-top:3px dotted #666"></div>
</div>

<section class="visit abs">
  <div class="panel-head">ABOUT YOUR VISIT</div>
  <ul>
    <li>Emergency Care</li><li>Accepted Health Plans</li><li>Pre-registration for Surgery</li><li>Lab Hours</li><li>Schedule a Lab Test</li><li>Find a Phone Number</li><li>Find A form</li><li>Pay Bill Online</li><li>Visitor Guide</li>
  </ul>
</section>

<section class="portal abs">
  <svg class="abs" style="left:8px;top:10px" width="36" height="44" viewBox="0 0 36 44"><path d="M20 2H4v40h16" fill="none" stroke="#fff" stroke-width="3"/><path d="M10 16h12V8l12 14-12 14v-8H10z" fill="#fff"/></svg>
  <div class="t">BRACKFIELD<br>PATIENT PORTAL</div>
  <div class="btn">LOGIN OR REGISTER</div>
</section>

<section class="resources abs">
  <div class="panel-head">PATIENT RESOURCES</div>
  <ul>
    <li><span class="i">+</span>Tips on chossing the Right Doctor</li>
    <li><span class="i">+</span>Billing, forms &amp; Medical Records</li>
    <li><span class="i">+</span>Making the most your Appointment</li>
  </ul>
</section>

<div class="news-tabs abs"></div>
<div class="tab-active abs">BH News</div>
<div class="tab abs">Upcoming Classes &amp; Events</div>
<section class="news-band abs"></section>

<svg class="hex" style="left:40px;top:776px" width="84" height="92" viewBox="0 0 84 92" role="img" aria-label="Photo of the hospital building"><polygon points="42,3 80,24 80,68 42,89 4,68 4,24" fill="#f4594b" stroke="#fff" stroke-width="3"/><polygon points="42,9 75,27 75,65 42,83 9,65 9,27" fill="url(#bld)"/><defs><linearGradient id="bld" x1="0" y1="0" x2="0" y2="1"><stop offset="0" stop-color="#9cc6e4"/><stop offset=".55" stop-color="#d6e2e6"/><stop offset="1" stop-color="#56695a"/></linearGradient></defs></svg>
<svg class="hex" style="left:186px;top:776px" width="84" height="92" viewBox="0 0 84 92" role="img" aria-label="Photo of the hospital building"><polygon points="42,3 80,24 80,68 42,89 4,68 4,24" fill="#f4594b" stroke="#fff" stroke-width="3"/><polygon points="42,9 75,27 75,65 42,83 9,65 9,27" fill="url(#bld)"/></svg>
<svg class="hex" style="left:330px;top:776px" width="84" height="92" viewBox="0 0 84 92" role="img" aria-label="Photo of the hospital building"><polygon points="42,3 80,24 80,68 42,89 4,68 4,24" fill="#f4594b" stroke="#fff" stroke-width="3"/><polygon points="42,9 75,27 75,65 42,83 9,65 9,27" fill="url(#bld)"/></svg>
<svg class="hex" style="left:479px;top:776px" width="84" height="92" viewBox="0 0 84 92" role="img" aria-label="Photo of the hospital building"><polygon points="42,3 80,24 80,68 42,89 4,68 4,24" fill="#f4594b" stroke="#fff" stroke-width="3"/><polygon points="42,9 75,27 75,65 42,83 9,65 9,27" fill="url(#bld)"/></svg>
<svg class="hex" style="left:625px;top:776px" width="84" height="92" viewBox="0 0 84 92" role="img" aria-label="Photo of the hospital building"><polygon points="42,3 80,24 80,68 42,89 4,68 4,24" fill="#f4594b" stroke="#fff" stroke-width="3"/><polygon points="42,9 75,27 75,65 42,83 9,65 9,27" fill="url(#bld)"/></svg>

<p class="story abs" style="left:16px;top:880px">Lorem Ipsum is simply dummy text of the printing and type-setting industry. Lorem Ipsum</p>
<p class="story abs" style="left:163px;top:880px">Lorem Ipsum is simply dummy text of the printing and type-setting industry. Lorem Ipsum</p>
<p class="story abs" style="left:306px;top:880px">Lorem Ipsum is simply dummy text of the printing and type-setting industry. Lorem Ipsum</p>
<p class="story abs" style="left:455px;top:880px">Lorem Ipsum is simply dummy text of the printing and type-setting industry. Lorem Ipsum</p>
<p class="story abs" style="left:602px;top:880px">Lorem Ipsum is simply dummy text of the printing and type-setting industry. Lorem Ipsum</p>
<a class="see-all abs" href="#">SEE ALL STORIES</a>

<footer class="footer abs"></footer>
<div class="field abs" style="left:70px;top:1000px;width:135px">Name</div>
<div class="field abs" style="left:70px;top:1041px;width:135px">Email</div>
<div class="field abs" style="left:247px;top:1000px;width:140px;border:none">Message</div>
<div class="msg abs"></div>
<div class="send abs">SEND</div>

<svg class="abs" style="left:522px;top:1010px" width="9" height="10" viewBox="0 0 10 10"><path d="M2 0l2 3-1 1c1 2 2 3 3 3l1-1 3 2-1 2C4 10 0 6 0 2z" fill="#777"/></svg>
<div class="contact abs" style="top:1004px;left:537px"><b>CALL US</b><span class="big">000 418-2270</span></div>
<svg class="abs" style="left:523px;top:1048px" width="8" height="11" viewBox="0 0 8 11"><path d="M4 0a4 4 0 0 1 4 4c0 3-4 7-4 7S0 7 0 4a4 4 0 0 1 4-4z" fill="#777"/><circle cx="4" cy="4" r="1.5" fill="#2b2b2b"/></svg>
<div class="contact abs" style="top:1042px;left:537px"><b>ADDRESS</b>4820 Larkspur Road, Suite 12,<br>Ferncastle, 90210</div>
<svg class="abs" style="left:522px;top:1093px" width="10" height="8" viewBox="0 0 10 8"><rect width="10" height="8" fill="#777"/><path d="M0 0l5 4 5-4" fill="none" stroke="#2b2b2b"/></svg>
<div class="contact abs" style="top:1086px;left:537px"><b>SAY HELLO</b>hello@brackfieldhospital.org</div>

<div class="footer-bottom abs"></div>
<nav class="bottom-links abs">Home &nbsp;|&nbsp; Our Services &nbsp;|&nbsp; Facilities &amp; Directions &nbsp;|&nbsp; Patient &amp; Visitor Information &nbsp;|&nbsp; Find a Doctor &nbsp;|&nbsp; Health &amp; Wellness</nav>
<span class="social abs" style="left:596px"></span>
<span class="social abs" style="left:619px"></span>
<span class="social abs" style="left:642px"></span>
<span class="social abs" style="left:665px"></span>
<span class="social abs" style="left:688px"></span>
<span class="social abs" style="left:711px"></span>
<div class="copy abs">©2014 BRACKFIELD HOSPITAL</div>

</body>
</html>
```